Yacht, Boats, Watersports company needs a redesign of business card

Hello Designers!
We are a Boat dealership company that sells fun in the water, we sell boats, Yachts, Kayaks and also yacht WaterSport toys. We are looking to redesign our business cards in to something a little bit more sophisticated. in a way that we can make better use of our company colors. I'm attaching a zipped file containing the company 3 sets of company logo which one is an horizontal another one is a vertical and also a chromed 3d logo. Also is included two set of business cards that we use and also some designs that i think it's interesting. We use PMS 2026c Orange and PMS 7687C Blue. I would like to see at least two different options with the orange as accent and also using blue as an accent color. It's really important for the business cards to have a font option and size that is legible to most people. Our current website is wwww.corvellamarine.com. Please visit if you want to have a better feeling of the Boat dealership
You can send Single sided or double side options. We are now using single sided but we may be open for a double side option if we really like the design.
Target Market(s)
Marine, boat sales, yacht sales, water toys sales/
Contact Information for Business Card
Name: Dale Pritchett
Address: 718 West Halden Lane,
Dania Beach, FL 33019
Phone: 954-382-7146
Fax: 954:382-7139
Cell: 954-451-8320
Email: 212@corvellamarine.com
Website: corvellamarine.com
Requirements
Must have
- the current information of the business card provided.
logo
use the PMS Colors
Nice to have
- a touch of elegance and sophistication but simple
Should not have
- should not have any typography that is hard to read, the card should be simple but yet sophisticated.

```html
<!DOCTYPE html>
<html lang="en">
<head>
<meta charset="utf-8">
<title>Corvella Marine — Business Card</title>
<link rel="stylesheet" href="https://fonts.googleapis.com/css2?family=Montserrat:wght@600;700&family=Open+Sans:wght@400;600&display=swap">
<style>
  :root {
    --pms-blue: #1a4c86;
    --pms-blue-deep: #163f70;
    --pms-orange: #ee5a24;
    --ink: #4a4a4a;
    --paper: #ffffff;
    --backdrop: #e9eaec;
  }
  * { box-sizing: border-box; margin: 0; padding: 0; }
  html, body { width: 1200px; height: 900px; overflow: hidden; }
  body {
    background: var(--backdrop);
    display: flex;
    flex-direction: column;
    align-items: center;
    justify-content: center;
    gap: 56px;
    font-family: "Open Sans", Arial, sans-serif;
  }
  .card {
    position: relative;
    width: 620px;
    height: 354px;
    overflow: hidden;
    box-shadow: 0 6px 18px rgba(0,0,0,0.18);
  }

  /* ---------- Front ---------- */
  .card-front { background: var(--paper); }
  .front-band {
    position: absolute; left: 12px; top: 0; bottom: 0; width: 62px;
    background: var(--pms-blue);
  }
  .front-corner {
    position: absolute; left: 74px; top: 0; width: 46px; height: 44px;
    background: var(--pms-orange);
  }
  .front-brand {
    position: absolute; left: 44px; top: 14px;
    display: flex; align-items: center; gap: 12px;
  }
  .brand-dot {
    width: 58px; height: 58px; border-radius: 50%;
    background: var(--paper);
    border: 5px solid var(--pms-blue);
    flex: none;
  }
  .brand-name {
    font-family: "Montserrat", Arial, sans-serif;
    font-weight: 700;
    font-size: 17px;
    letter-spacing: 1.5px;
    text-transform: uppercase;
    color: var(--pms-blue);
    margin-top: 44px;
    white-space: nowrap;
  }
  .contact {
    position: absolute; left: 96px; top: 112px;
    color: var(--ink);
  }
  .contact-name {
    font-family: "Montserrat", Arial, sans-serif;
    font-weight: 700;
    font-size: 23px;
    letter-spacing: 1px;
    text-transform: uppercase;
    color: var(--pms-blue);
    white-space: nowrap;
  }
  .contact-rule {
    width: 12px; height: 2px; background: var(--pms-orange);
    margin: 6px 0 8px;
  }
  .contact-address { font-size: 13.5px; line-height: 1.35; }
  .contact-list { list-style: none; margin-top: 4px; }
  .contact-list li {
    display: flex; align-items: center; gap: 7px;
    font-size: 13.5px; line-height: 1.45;
  }
  .contact-icon { width: 13px; height: 13px; flex: none; }
  .contact-web { font-size: 13.5px; margin-top: 2px; }
  .contact-web strong { color: var(--pms-blue); font-weight: 600; }

  /* ---------- Back ---------- */
  .card-back {
    background: linear-gradient(135deg, var(--pms-blue) 0%, var(--pms-blue-deep) 100%);
    display: flex; align-items: center; justify-content: center; gap: 18px;
  }
  .back-dot {
    width: 74px; height: 74px; border-radius: 50%;
    border: 7px solid var(--pms-orange);
    flex: none;
  }
  .back-name {
    font-family: "Montserrat", Arial, sans-serif;
    font-weight: 700;
    font-size: 34px;
    letter-spacing: 3px;
    text-transform: uppercase;
    color: var(--paper);
    white-space: nowrap;
  }
</style>
</head>
<body>

  <section class="card card-front" aria-label="Business card front">
    <div class="front-band"></div>
    <div class="front-corner"></div>

    <div class="front-brand">
      <span class="brand-dot" aria-hidden="true"></span>
      <span class="brand-name">Corvella Marine</span>
    </div>

    <div class="contact">
      <h1 class="contact-name">Dale Pritchett</h1>
      <div class="contact-rule"></div>
      <p class="contact-address">718 West Halden Lane,<br>Dania Beach, FL 33019</p>
      <ul class="contact-list">
        <li>
          <svg class="contact-icon" viewBox="0 0 14 14" aria-hidden="true"><circle cx="7" cy="7" r="7" fill="#ee5a24"/><path d="M4.5 3.5l1.6 0 .6 1.8-1 .8a5 5 0 0 0 2.2 2.2l.8-1 1.8.6v1.6c-3.4.3-6.3-2.6-6-6z" fill="#fff"/></svg>
          954-382-7146
        </li>
        <li>
          <svg class="contact-icon" viewBox="0 0 14 14" aria-hidden="true"><circle cx="7" cy="7" r="7" fill="#ee5a24"/><rect x="4.5" y="3.3" width="5" height="2.4" fill="#fff"/><rect x="3.4" y="6.1" width="7.2" height="3" rx=".6" fill="#fff"/><rect x="4.5" y="9.4" width="5" height="1.5" fill="#fff"/></svg>
          954:382-7139
        </li>
        <li>
          <svg class="contact-icon" viewBox="0 0 14 14" aria-hidden="true"><circle cx="7" cy="7" r="7" fill="#ee5a24"/><rect x="4.8" y="3" width="4.4" height="8" rx=".8" fill="#fff"/><rect x="5.5" y="4" width="3" height="5" fill="#ee5a24"/></svg>
          954-451-8320
        </li>
        <li>
          <svg class="contact-icon" viewBox="0 0 14 14" aria-hidden="true"><circle cx="7" cy="7" r="7" fill="#ee5a24"/><rect x="3.5" y="4.5" width="7" height="5" fill="#fff"/><path d="M3.5 4.5L7 7.3l3.5-2.8" fill="none" stroke="#ee5a24" stroke-width=".8"/></svg>
          212@corvellamarine.com
        </li>
      </ul>
      <p class="contact-web">www.<strong>corvellamarine.com</strong></p>
    </div>
  </section>

  <section class="card card-back" aria-label="Business card back">
    <span class="back-dot" aria-hidden="true"></span>
    <span class="back-name">Corvella Marine</span>
  </section>

</body>
</html>
```